Professional Vehicle Wrap Design | 2020 Brant Corvan | RV Tolley

We are seeking a full van wrap design for a 2020 Brant Corvan K-240 Cargo Van that will represent RV Tolley. The primary color for this wrap should be sky blue to align with their branding and create a bold, professional appearance that stands out on the road.

Vehicle Details:

2020 Brant Corvan K-240

Low Roof

129.9" Wheelbase (Regular)

Cargo configuration with sliding door on the right and dual rear doors (no side windows)

Design Requirements:

The wrap should feature sky blue as the dominant color.

Incorporate the RV Tolley logo and branding elements (logo files provided).

Design should be clean, professional, and highly visible for branding impact.

Avoid placing important text or graphics across sliding doors, seams, or complex panel curves to ensure durability and readability.

The design should complement the cargo van’s panel layout and utilize the full available wrap area effectively.

Included Files:
Download all project assets here: https://www.filevaultex.com/share/qk7m2ds9pt4xw8rn3bv/ZTyLpw82kdmRqa?key=x4n8v2c7q1w9e&dl=0

We look forward to seeing creative and impactful wrap designs that help RV Tolley stand out.
*Final Files must be exported on the template provided
https://www.rvtolley.com/

Target Market(s)

RV Tolley serves homeowners, businesses, and property managers in Florence, AL. The wrap should convey professionalism and reliability to attract local clients seeking quality contracting and HVAC services.

Industry/Entity Type

RV Tolley operates in the HVAC and general contracting industry, providing heating, ventilation, and air conditioning services.

Colors

Requirements
Must have
• The wrap must feature sky blue as the primary color and prominently display the RV Tolley logo. The design should be bold, professional, and clean, avoiding critical text or graphics on sliding doors and seams. It should effectively use the full cargo van wrap area and ensure high visibility and easy brand recognition on the road.
Nice to have
• It would be great if the design incorporates subtle icons or visuals representing RV Tolley’s services, uses complementary colors to enhance the sky blue, and includes space for contact information without cluttering the overall look.
Should not have
• The design should not include overly busy patterns or small text that’s hard to read from a distance. Avoid placing important information over sliding door seams or complex curves, and steer clear of colors that clash with the primary sky blue.

```html
<!DOCTYPE html>
<html lang="en">
<head>
<meta charset="utf-8">
<title>RV Tolley – Brant Corvan Wrap</title>
<link rel="stylesheet" href="https://fonts.googleapis.com/css2?family=Montserrat:wght@700;800&family=Barlow+Condensed:ital,wght@1,700&display=swap">
<style>
  :root {
    --sky: #0399dc;
    --navy: #0b4a96;
    --white: #ffffff;
    --page: #ffffff;
  }
  html, body { margin: 0; padding: 0; overflow: hidden; background: var(--page); }
  .canvas { position: relative; width: 1200px; height: 2580px; }
  .wrap-art { position: absolute; inset: 0; }
  .panel-fill { fill: var(--sky); }
  .oval { fill: var(--white); }
  .brand-name { font-family: "Montserrat", sans-serif; font-weight: 800; fill: var(--navy); }
  .brand-dot { fill: var(--navy); }
  .phone-side { font-family: "Barlow Condensed", sans-serif; font-style: italic; font-weight: 700; fill: var(--white); }
  .phone-rear { font-family: "Montserrat", sans-serif; font-weight: 700; fill: var(--white); }
  .site { font-family: "Montserrat", sans-serif; font-weight: 700; fill: var(--white); }
</style>
</head>
<body>
<div class="canvas">
  <svg class="wrap-art" width="1200" height="2580" viewBox="0 0 1200 2580">
    <defs>
      <clipPath id="side-view-clip"><rect x="68" y="118" width="1057" height="350" rx="40"/></clipPath>
      <clipPath id="rear-view-clip"><rect x="295" y="625" width="610" height="400" rx="30"/></clipPath>
      <clipPath id="side-template-clip"><rect x="48" y="1320" width="1102" height="440"/></clipPath>
      <clipPath id="rear-template-clip"><rect x="253" y="1842" width="692" height="553"/></clipPath>
    </defs>

    <!-- Side elevation, flat -->
    <g class="side-view" clip-path="url(#side-view-clip)">
      <rect class="panel-fill" x="68" y="118" width="1057" height="350"/>
      <ellipse class="oval" cx="760" cy="180" rx="360" ry="110" transform="rotate(-18 760 180)"/>
      <circle class="brand-dot" cx="530" cy="225" r="13"/>
      <text class="brand-name" x="552" y="246" font-size="62">RV Tolley</text>
      <text class="phone-side" x="1070" y="332" font-size="42" text-anchor="end">(256) 555-0148</text>
      <text class="site" x="648" y="364" font-size="23" text-anchor="middle">www.rvtolley.com</text>
    </g>

    <!-- Rear elevation, flat -->
    <g class="rear-view" clip-path="url(#rear-view-clip)">
      <rect class="panel-fill" x="295" y="625" width="610" height="400"/>
      <ellipse class="oval" cx="605" cy="778" rx="240" ry="112" transform="rotate(-12 605 778)"/>
      <circle class="brand-dot" cx="425" cy="790" r="11"/>
      <text class="brand-name" x="445" y="808" font-size="54">RV Tolley</text>
      <text class="phone-rear" x="748" y="940" font-size="25" text-anchor="middle">(256) 555-0148</text>
      <text class="site" x="748" y="962" font-size="16" text-anchor="middle">www.rvtolley.com</text>
    </g>

    <!-- Side print template -->
    <g class="side-template" clip-path="url(#side-template-clip)">
      <rect class="panel-fill" x="48" y="1320" width="1102" height="440"/>
      <ellipse class="oval" cx="760" cy="1450" rx="360" ry="110" transform="rotate(-18 760 1450)"/>
      <circle class="brand-dot" cx="530" cy="1495" r="13"/>
      <text class="brand-name" x="552" y="1516" font-size="62">RV Tolley</text>
      <text class="phone-side" x="1070" y="1602" font-size="42" text-anchor="end">(256) 555-0148</text>
      <text class="site" x="648" y="1634" font-size="23" text-anchor="middle">www.rvtolley.com</text>
    </g>

    <!-- Rear print template -->
    <g class="rear-template" clip-path="url(#rear-template-clip)">
      <rect class="panel-fill" x="253" y="1842" width="692" height="553"/>
      <ellipse class="oval" cx="605" cy="2048" rx="240" ry="112" transform="rotate(-12 605 2048)"/>
      <circle class="brand-dot" cx="425" cy="2060" r="11"/>
      <text class="brand-name" x="445" y="2078" font-size="54">RV Tolley</text>
      <text class="phone-rear" x="748" y="2210" font-size="25" text-anchor="middle">(256) 555-0148</text>
      <text class="site" x="748" y="2232" font-size="16" text-anchor="middle">www.rvtolley.com</text>
    </g>
  </svg>
</div>
</body>
</html>
```